Design a 1 mobile profile page for social personal feedback app

Project name is Glimmer you.
I need a 1 mobile profile page
In this page I want show the likes and dislikes of a person.

There are multi categories on this such as
A)
Doing Sports.
Going out
Reading
Eating
Talking about
Watching
Dreaming about
Having fun
Spending money

b)
Angry if.
Love to
Believe in.
Afraid of
Proud of
Laughing to

c) Hero

Design the page with more icons and gifs .
The page has also picture .age ,gender ,where

```html
<!DOCTYPE html>
<html lang="en">
<head>
<meta charset="UTF-8">
<title>Glimmer you – Profile</title>
<link href="https://fonts.googleapis.com/css2?family=Inter:wght@400;500;600&display=swap" rel="stylesheet">
<style>
  :root {
    --bg: #2c2c2c;
    --panel: #1f1f1f;
    --card-top: #2e2e2e;
    --card-bottom: #1c1c1c;
    --card-border: #4a4a4a;
    --text: #ffffff;
    --muted: #8a8a8a;
    --soft: #9c9c9c;
    --icon: #8c8c8c;
    --rule: #4a4a4a;
    --title: #7b6cf0;
    --ring: #8d2cf0;
  }
  * { box-sizing: border-box; margin: 0; padding: 0; }
  html, body { width: 1085px; height: 1200px; overflow: hidden; }
  body {
    background: var(--bg);
    font-family: "Inter", sans-serif;
    color: var(--text);
    position: relative;
  }
  .brand-title {
    position: absolute; top: 92px; left: 0; width: 100%;
    text-align: center; font-size: 48px; font-weight: 500;
    color: var(--title);
  }
  .phone {
    position: absolute; background: var(--panel);
    border-radius: 4px; overflow: hidden;
  }
  .phone--categories { left: 187px; top: 204px; width: 295px; height: 914px; }
  .phone--edit { left: 571px; top: 260px; width: 327px; height: 705px; }

  .cover {
    position: absolute; left: 0; top: 0; width: 100%;
    background:
      linear-gradient(180deg, rgba(31,31,31,0) 60%, var(--panel) 100%),
      linear-gradient(90deg, #3c4650 0%, #8c98a4 30%, #b7bcc0 55%, #6f5d52 80%, #8b4a35 100%);
  }
  .phone--categories .cover { height: 158px; }
  .phone--edit .cover { height: 174px; }

  .avatar {
    position: absolute; border-radius: 50%;
    border: 3px solid var(--ring);
    background: radial-gradient(circle at 55% 40%, #1f3d5c 0%, #0e0e1a 55%, #3a0d2a 100%);
    transform: translate(-50%, -50%);
  }
  .phone--categories .avatar { left: 148px; top: 125px; width: 80px; height: 80px; }
  .phone--edit .avatar { left: 164px; top: 139px; width: 88px; height: 88px; }

  .name, .role { position: absolute; width: 100%; text-align: center; }
  .name { font-weight: 500; }
  .role { color: var(--muted); }
  .phone--categories .name { top: 176px; font-size: 15px; }
  .phone--categories .role { top: 197px; font-size: 10px; }
  .phone--edit .name { top: 196px; font-size: 17px; }
  .phone--edit .role { top: 219px; font-size: 11px; }

  .stat {
    position: absolute; width: 90px; margin-left: -45px; text-align: center;
    color: var(--soft); font-size: 9px; line-height: 11px;
  }
  .stat svg { display: block; margin: 0 auto 6px; fill: var(--icon); }
  .phone--categories .stat { top: 234px; }
  .phone--edit .stat { top: 262px; font-size: 10px; line-height: 12px; }
  .stat-divider { position: absolute; width: 1px; height: 8px; background: #555; }
  .phone--categories .stat-divider { top: 262px; }
  .phone--edit .stat-divider { top: 292px; }

  .section-title { position: absolute; font-size: 15px; font-weight: 500; }
  .phone--categories .section-title { left: 17px; top: 294px; }
  .phone--edit .section-title { left: 19px; top: 330px; }

  .category-card {
    position: absolute; left: 17px; width: 259px; height: 52px;
    border: 1px solid var(--card-border); border-radius: 6px;
    background: linear-gradient(90deg, var(--card-top), var(--card-bottom));
  }
  .category-name { position: absolute; left: 16px; top: 11px; font-size: 11px; }
  .category-count { position: absolute; left: 16px; top: 29px; font-size: 8px; color: var(--soft); }
  .category-count span + span { margin-left: 6px; }
  .category-icon {
    position: absolute; right: 24px; top: 6px; width: 38px; height: 38px;
    border-radius: 50%; background: #2f2f2f;
  }
  .category-icon span { position: absolute; inset: 8px; border-radius: 50%; }

  .view-all { position: absolute; left: 0; width: 100%; top: 836px; text-align: center; font-size: 10px; color: var(--soft); }

  .field {
    position: absolute; left: 19px; width: 287px; height: 22px;
    border-bottom: 1px solid var(--rule); font-size: 12px; color: var(--muted);
  }
</style>
</head>
<body>
  <h1 class="brand-title">Glimmer you</h1>

  <section class="phone phone--categories">
    <div class="cover" role="img" aria-label="Cover photo of the user working at a laptop in a bright office"></div>
    <div class="avatar" role="img" aria-label="Profile portrait in neon blue and magenta light"></div>
    <div class="name">Adam Brooks</div>
    <div class="role">UX Designer</div>

    <div class="stat" style="left:53px">
      <svg width="18" height="20" viewBox="0 0 18 20"><circle cx="9" cy="5" r="5"/><path d="M0 20c0-6 4-9 9-9s9 3 9 9z"/></svg>Personal Info
    </div>
    <span class="stat-divider" style="left:104px"></span>
    <div class="stat" style="left:152px">
      <svg width="22" height="20" viewBox="0 0 22 20"><rect x="0" y="8" width="5" height="12"/><path d="M7 8l5-8c2 0 3 1 3 3l-1 4h6c1 0 2 1 2 2l-2 9c0 1-1 2-2 2H7z"/></svg>1.7k Likes
    </div>
    <span class="stat-divider" style="left:198px"></span>
    <div class="stat" style="left:246px">
      <svg width="22" height="20" viewBox="0 0 22 20"><g transform="rotate(180 11 10)"><rect x="0" y="8" width="5" height="12"/><path d="M7 8l5-8c2 0 3 1 3 3l-1 4h6c1 0 2 1 2 2l-2 9c0 1-1 2-2 2H7z"/></g></svg>10 DisLikes
    </div>

    <h2 class="section-title">Categories</h2>

    <div class="category-card" style="top:328px"><div class="category-name">Doing Sports</div><div class="category-count"><span>10 likes</span><span>0 dislikes</span></div><div class="category-icon" role="img" aria-label="Sports icon"><span style="background:#3c6fd8"></span></div></div>
    <div class="category-card" style="top:391px"><div class="category-name">Going Out</div><div class="category-count"><span>0 likes</span><span>1 dislikes</span></div><div class="category-icon" role="img" aria-label="Going out icon"><span style="background:#d83a3a"></span></div></div>
    <div class="category-card" style="top:454px"><div class="category-name">Reading</div><div class="category-count"><span>13 likes</span><span>0 dislikes</span></div><div class="category-icon" role="img" aria-label="Reading icon"><span style="background:#e0a83a"></span></div></div>
    <div class="category-card" style="top:515px"><div class="category-name">Eating</div><div class="category-count"><span>0 likes</span><span>0 dislikes</span></div><div class="category-icon" role="img" aria-label="Eating icon"><span style="background:#3aa0a8"></span></div></div>
    <div class="category-card" style="top:577px"><div class="category-name">Watching</div><div class="category-count"><span>1 likes</span><span>0 dislikes</span></div><div class="category-icon" role="img" aria-label="Watching icon"><span style="background:#e08a30"></span></div></div>
    <div class="category-card" style="top:640px"><div class="category-name">Talking About</div><div class="category-count"><span>10 likes</span><span>0 dislikes</span></div><div class="category-icon" role="img" aria-label="Talking icon"><span style="background:#4ab8b0"></span></div></div>
    <div class="category-card" style="top:701px"><div class="category-name">Dreaming About</div><div class="category-count"><span>100 likes</span><span>0 dislikes</span></div><div class="category-icon" role="img" aria-label="Dreaming icon"><span style="background:#8a6ad8"></span></div></div>
    <div class="category-card" style="top:764px"><div class="category-name">Having Fun</div><div class="category-count"><span>10 likes</span><span>0 dislikes</span></div><div class="category-icon" role="img" aria-label="Having fun icon"><span style="background:#e0b070"></span></div></div>

    <div class="view-all">View all</div>
  </section>

  <section class="phone phone--edit">
    <div class="cover" role="img" aria-label="Cover photo of the user working at a laptop in a bright office"></div>
    <div class="avatar" role="img" aria-label="Profile portrait in neon blue and magenta light"></div>
    <div class="name">Adam Brooks</div>
    <div class="role">UX Designer</div>

    <div class="stat" style="left:59px">
      <svg width="20" height="22" viewBox="0 0 18 20"><circle cx="9" cy="5" r="5"/><path d="M0 20c0-6 4-9 9-9s9 3 9 9z"/></svg>Personal Info
    </div>
    <span class="stat-divider" style="left:115px"></span>
    <div class="stat" style="left:169px">
      <svg width="24" height="22" viewBox="0 0 22 20"><rect x="0" y="8" width="5" height="12"/><path d="M7 8l5-8c2 0 3 1 3 3l-1 4h6c1 0 2 1 2 2l-2 9c0 1-1 2-2 2H7z"/></svg>1.7k Likes
    </div>
    <span class="stat-divider" style="left:220px"></span>
    <div class="stat" style="left:273px">
      <svg width="24" height="22" viewBox="0 0 22 20"><g transform="rotate(180 11 10)"><rect x="0" y="8" width="5" height="12"/><path d="M7 8l5-8c2 0 3 1 3 3l-1 4h6c1 0 2 1 2 2l-2 9c0 1-1 2-2 2H7z"/></g></svg>10 DisLikes
    </div>

    <h2 class="section-title">Edit Profile</h2>
    <div class="field" style="top:366px">United state, America</div>
    <div class="field" style="top:402px">Male</div>
    <div class="field" style="top:437px">20 yrs old</div>
    <div class="field" style="top:473px">English</div>
    <div class="field" style="top:509px">Senior ux designer</div>
  </section>
</body>
</html>
```